New Solo Law Office Needs Business Card/Letterhead Design

I am starting a solo law office called "Law Office of Brian Kolmer, PLLC" in Tucson, Arizona. I will be doing criminal defense trial work. More than a logo with any sort of icon, I am really just looking for the name of the company to be displayed in a sleek, minimalist but interesting sort of way, with a format and font type that communicates professionalism. It can be in color, but doesn't have to be, and I am thinking blue and/or red accents colors. I'd like it to convey that I am passionate, dependable and willing to fight. For the business card, I envision sort of higher quality card material, and maybe some embossing or raised print. I will want to include my company name, name, phone and fax numbers, email and website addresses. For the letterhead, I will want to be able to use the same sort of font/formatting design as on the business card.
Industry/Entity Type
Business
Contact Information for Business Card
Law Office of Brian Kolmer, PLLC
Brian Kolmer
brian@kolmer-law.example
www.kolmer-law.example
(I do not yet have an established phone or fax number, so please put in some place holder numbers for the formatting, and I can add the actual numbers in before I print.)
Colors
Designer to choose colors to be used in the design.
Look and feel
Each slider illustrates characteristics of the customer's brand and the style your logo design should communicate.

```html
<!DOCTYPE html>
<html lang="en">
<head>
<meta charset="utf-8">
<title>Law Office of Brian Kolmer, PLLC – Business Card</title>
<link rel="stylesheet" href="https://fonts.googleapis.com/css2?family=Raleway:wght@500;600;700&family=Open+Sans:wght@400&display=swap">
<style>
  :root {
    --paper-light: #f7f8fa;
    --paper-mid: #eceef1;
    --paper-shade: #dcdfe4;
    --title-grey: #5b5d61;
    --band-blue: #22408f;
    --accent-red: #f25a4b;
    --white: #ffffff;
  }
  * { margin: 0; padding: 0; box-sizing: border-box; }
  html, body { width: 1200px; height: 686px; overflow: hidden; background: var(--white); }
  .card { position: relative; width: 1200px; height: 686px; overflow: hidden; }

  .hero {
    position: absolute; left: 0; top: 0; width: 1200px; height: 397px;
    background:
      radial-gradient(ellipse 380px 300px at 1000px 190px, var(--paper-shade), transparent 70%),
      linear-gradient(180deg, var(--paper-light) 0%, var(--paper-mid) 100%);
  }
  .firm-name {
    position: absolute; left: 135px; top: 148px;
    font-family: "Raleway", sans-serif; font-weight: 600;
    font-size: 57px; line-height: 71px; letter-spacing: 2px;
    text-transform: uppercase; color: var(--title-grey);
    text-shadow: 1px 1px 0 #ffffff, 2px 3px 3px rgba(0,0,0,0.35);
  }

  .contact-band {
    position: absolute; left: 0; top: 397px; width: 1200px; height: 269px;
    background: var(--band-blue); color: var(--white);
  }
  .person { position: absolute; left: 135px; top: 77px; font-family: "Raleway", sans-serif; }
  .person-name { font-weight: 700; font-size: 38px; letter-spacing: 1.5px; line-height: 44px; text-transform: uppercase; }
  .person-role { font-weight: 700; font-size: 29px; letter-spacing: 1px; line-height: 36px; }

  .contact-list { position: absolute; left: 583px; top: 22px; list-style: none; }
  .contact-item { display: flex; align-items: center; height: 55.5px; }
  .contact-icon { width: 36px; height: 36px; margin-right: 12px; flex: none; }
  .contact-text { font-family: "Raleway", sans-serif; font-weight: 500; font-size: 34px; }
  .contact-text.number { font-family: "Open Sans", sans-serif; font-weight: 400; font-size: 32px; }

  .accent-stripe { position: absolute; left: 0; top: 666px; width: 1200px; height: 20px; background: var(--accent-red); }
</style>
</head>
<body>
<div class="card">
  <div class="hero" role="img" aria-label="Soft-focus photograph of brass scales of justice in a courtroom"></div>
  <h1 class="firm-name">Law Office of<br>Brian Kolmer, PLLC</h1>

  <section class="contact-band">
    <div class="person">
      <p class="person-name">Brian Kolmer</p>
      <p class="person-role">Designation here</p>
    </div>
    <ul class="contact-list">
      <li class="contact-item">
        <svg class="contact-icon" viewBox="0 0 36 36" aria-hidden="true">
          <circle cx="18" cy="18" r="16.5" fill="none" stroke="#fff" stroke-width="1.6"/>
          <path d="M12 9.5c1-.6 2-.4 2.6.5l2 3c.5.8.3 1.7-.4 2.2l-1.3 1c.8 2 2.3 3.6 4.3 4.5l1-1.3c.6-.7 1.5-.8 2.2-.3l3 2c.9.6 1.1 1.7.4 2.6l-1.2 1.4c-.8.9-2.1 1.2-3.2.8-5-1.9-9-5.9-10.8-10.9-.4-1.1 0-2.4.9-3.1z" fill="#fff"/>
        </svg>
        <span class="contact-text number">91-55501470</span>
      </li>
      <li class="contact-item">
        <svg class="contact-icon" viewBox="0 0 36 36" aria-hidden="true">
          <circle cx="18" cy="18" r="16.5" fill="none" stroke="#fff" stroke-width="1.6"/>
          <rect x="12" y="9" width="12" height="6" fill="#fff"/>
          <rect x="9" y="14" width="18" height="10" rx="2" fill="#fff"/>
          <rect x="12" y="20" width="12" height="7" fill="#fff" stroke="#22408f" stroke-width="1.4"/>
          <line x1="14" y1="23" x2="22" y2="23" stroke="#22408f" stroke-width="1.2"/>
        </svg>
        <span class="contact-text number">231-5550148</span>
      </li>
      <li class="contact-item">
        <svg class="contact-icon" viewBox="0 0 36 36" aria-hidden="true">
          <circle cx="18" cy="18" r="16.5" fill="none" stroke="#fff" stroke-width="1.6"/>
          <rect x="9.5" y="12" width="17" height="12" rx="1.2" fill="#fff"/>
          <path d="M10 12.8l8 6.2 8-6.2" fill="none" stroke="#22408f" stroke-width="1.4"/>
        </svg>
        <span class="contact-text">brian@kolmer-law.example</span>
      </li>
      <li class="contact-item">
        <svg class="contact-icon" viewBox="0 0 36 36" aria-hidden="true">
          <circle cx="18" cy="18" r="16.5" fill="none" stroke="#fff" stroke-width="1.6"/>
          <g fill="none" stroke="#fff" stroke-width="1.4">
            <circle cx="18" cy="18" r="9"/>
            <ellipse cx="18" cy="18" rx="4" ry="9"/>
            <line x1="9" y1="18" x2="27" y2="18"/>
            <path d="M10.5 13.5h15M10.5 22.5h15"/>
          </g>
        </svg>
        <span class="contact-text">www.kolmer-law.example</span>
      </li>
    </ul>
  </section>

  <div class="accent-stripe"></div>
</div>
</body>
</html>
```